Business Card for Graphic Design Firm

This project is for a new graphic design firm based in New Jersey called Velmoric. We outsource graphic design and marketing jobs. We want to communicate that this is a professional company but it as well creative and artistic. This card may be used as a horizontal double sided paper card or a vertical single sided translucent card so feel free to submit designs in whichever format or both.
Updates

Reason: Extending the deadline because I'm not exactly satisfied with the designs so far.

Please view the updated project brief

Target Market(s)

Adults aged 25-60

Industry/Entity Type

Graphic Design

Font styles to use
Serif
Sans Serif

Requirements
Nice to have
• Maybe a triangular pattern around the edges similar to our logo

```html
<!DOCTYPE html>
<html lang="en">
<head>
<meta charset="utf-8">
<title>Velmoric — Business Card</title>
<link href="https://fonts.googleapis.com/css2?family=Questrial&family=Nunito:wght@600&display=swap" rel="stylesheet">
<style>
  :root {
    --backdrop: #2b2c2e;
    --card: #8e9194;
    --card-edge: #a7aaad;
    --ink: #ffffff;
    --ink-soft: #f1f2f3;
    --teal-light: #6ec3dc;
    --teal: #14a3b3;
    --gold: #e6ad22;
    --orange: #e57d2c;
  }
  * { margin: 0; padding: 0; box-sizing: border-box; }
  html, body {
    width: 1200px;
    height: 900px;
    overflow: hidden;
    background: var(--backdrop);
  }
  .canvas {
    position: relative;
    width: 1200px;
    height: 900px;
  }
  .card {
    position: absolute;
    left: 100px;
    top: 160px;
    width: 1000px;
    height: 580px;
    border-radius: 28px;
    background: var(--card);
    border: 2px solid var(--card-edge);
    overflow: hidden;
    font-family: "Questrial", "Helvetica Neue", Arial, sans-serif;
    color: var(--ink);
  }
  .card__pattern {
    position: absolute;
    left: 0;
    top: 0;
    width: 420px;
    height: 580px;
  }
  .card__info {
    position: absolute;
    right: 90px;
    text-align: right;
    line-height: 1.3;
  }
  .contact {
    top: 70px;
    font-size: 25px;
    color: var(--ink-soft);
  }
  .contact__name {
    text-transform: uppercase;
    letter-spacing: 0.04em;
  }
  .wordmark {
    position: absolute;
    right: 90px;
    top: 240px;
    font-family: "Nunito", "Helvetica Neue", Arial, sans-serif;
    font-weight: 600;
    font-size: 80px;
    letter-spacing: 0.08em;
    text-transform: uppercase;
    color: var(--ink);
  }
  .address {
    top: 400px;
    font-size: 27px;
  }
</style>
</head>
<body>
<main class="canvas">
  <article class="card">
    <svg class="card__pattern" viewBox="0 0 420 580" role="img" aria-label="Geometric triangle pattern in teal, blue, gold and orange">
      <defs>
        <linearGradient id="pattern-tones" x1="0" y1="0" x2="0" y2="1">
          <stop offset="0" stop-color="var(--teal)" stop-opacity="0.85"/>
          <stop offset="0.4" stop-color="var(--teal-light)" stop-opacity="0.75"/>
          <stop offset="0.6" stop-color="var(--gold)" stop-opacity="0.8"/>
          <stop offset="1" stop-color="var(--orange)" stop-opacity="0.85"/>
        </linearGradient>
      </defs>
      <rect x="130" y="0" width="290" height="580" fill="url(#pattern-tones)"/>
      <rect x="0" y="0" width="130" height="580" fill="#b3b6b9" opacity="0.5"/>
    </svg>

    <div class="card__info contact">
      <p class="contact__name">Dana Merrow</p>
      <p>managing director</p>
      <p>dmerrow@velmoric.com</p>
      <p>555 014 27 90</p>
    </div>

    <h1 class="wordmark">Velmoric</h1>

    <div class="card__info address">
      <p>48 Harbor Lane, Eastfield</p>
      <p>New Jersey 07012</p>
      <p>www.velmoric.com</p>
    </div>
  </article>
</main>
</body>
</html>
```